The Brightwater Compass Business Card

We need an attractive business card with the logo that we bought from ArtVantly last year.
Our mission is to contribute to change the way today's leaders manage business companies bringing value to the workplace and helping them to build a new model of creating wealth.
Our logo is clear about our values : we seek Positive Change through People and are convinced that the pursuit of individual well-being and the chase of economic results can converge with the right management.
Management Consulting
Corinne Fabrelle
+34 612 98 70 31
corinne.fabrelle@thebrightwatercompass-mail.net
www.thebrightwatercompass-mail.net

```html
<!DOCTYPE html>
<html lang="en">
<head>
<meta charset="utf-8">
<title>The Brightwater Compass – Business Card</title>
<link rel="stylesheet" href="https://fonts.googleapis.com/css2?family=Arimo:wght@400;700&display=swap">
<style>
  :root {
    --teal: #0f807b;
    --teal-deep: #0a6a66;
    --white: #ffffff;
    --paper: #f4f5f5;
    --backdrop: #2a2a2a;
  }
  * { box-sizing: border-box; margin: 0; padding: 0; }
  html, body {
    width: 1200px; height: 997px; overflow: hidden;
    background: var(--backdrop);
    font-family: "Arimo", Arial, sans-serif;
  }
  .stage {
    width: 1200px; height: 997px;
    display: flex; flex-direction: column;
    align-items: center; justify-content: center; gap: 60px;
  }
  .card {
    position: relative;
    width: 660px; height: 377px;
    border-radius: 22px;
    overflow: hidden;
  }

  /* Front: white top, striped teal lower band with contact details */
  .card--front {
    background: linear-gradient(to bottom,
      var(--paper) 0, var(--white) 44%,
      var(--teal) 44%, var(--teal) calc(44% + 4px),
      var(--white) calc(44% + 4px), var(--white) calc(44% + 9px),
      var(--teal) calc(44% + 9px), var(--teal) calc(44% + 13px),
      var(--white) calc(44% + 13px), var(--white) calc(44% + 18px),
      var(--teal) calc(44% + 18px), var(--teal-deep) 100%);
  }
  .card--front .brand {
    position: absolute; top: 52px; left: 0; right: 0;
    color: var(--teal);
  }
  .card--front .contact {
    position: absolute; top: 196px; left: 0; right: 0;
    text-align: center; color: var(--white);
  }
  .contact__name { font-weight: 700; font-size: 19px; letter-spacing: 1px; text-transform: uppercase; }
  .contact__role { font-weight: 700; font-size: 12px; letter-spacing: 1px; text-transform: uppercase; margin-top: 4px; }
  .contact__line { font-size: 13px; margin-top: 10px; letter-spacing: .3px; }
  .contact__line + .contact__line { margin-top: 5px; }
  .contact__web { font-weight: 700; letter-spacing: 1.6px; }

  /* Brand name, set plainly with a circle mark */
  .brand {
    display: flex; flex-direction: column; align-items: center; gap: 14px;
  }
  .brand__mark {
    width: 46px; height: 46px; border-radius: 50%;
    background: currentColor;
  }
  .brand__name {
    font-weight: 400; font-size: 26px; letter-spacing: 3px;
    text-transform: uppercase; text-align: center; line-height: 1.25;
  }

  /* Back: teal field with brand, stripes, white tagline strip */
  .card--back {
    background: linear-gradient(to bottom,
      var(--teal-deep) 0, var(--teal) 68%,
      var(--white) 68%, var(--white) calc(68% + 5px),
      var(--teal) calc(68% + 5px), var(--teal) calc(68% + 9px),
      var(--white) calc(68% + 9px), var(--white) calc(68% + 14px),
      var(--teal) calc(68% + 14px), var(--teal) calc(68% + 18px),
      var(--paper) calc(68% + 18px), var(--white) 100%);
  }
  .card--back .brand {
    position: absolute; top: 54px; left: 0; right: 0;
    color: var(--white);
  }
  .card--back .brand__mark { width: 64px; height: 64px; }
  .card--back .brand__name { font-size: 34px; letter-spacing: 4px; }
  .tagline {
    position: absolute; left: 0; right: 0; bottom: 0; height: 102px;
    display: flex; align-items: center; justify-content: center;
    color: var(--teal); font-weight: 700; font-size: 20px; letter-spacing: 1px;
    text-transform: uppercase;
  }
</style>
</head>
<body>
  <main class="stage">
    <section class="card card--front" aria-label="Business card front">
      <div class="brand">
        <span class="brand__mark"></span>
        <span class="brand__name">The Brightwater Compass</span>
      </div>
      <div class="contact">
        <p class="contact__name">Corinne Fabrelle</p>
        <p class="contact__role">Founder</p>
        <p class="contact__line">+34 612 98 70 31</p>
        <p class="contact__line">corinne.fabrelle@thebrightwatercompass-mail.net</p>
        <p class="contact__line contact__web">www.thebrightwatercompass-mail.net</p>
      </div>
    </section>

    <section class="card card--back" aria-label="Business card back">
      <div class="brand">
        <span class="brand__mark"></span>
        <span class="brand__name">The Brightwater Compass</span>
      </div>
      <p class="tagline">Choose to lead it better</p>
    </section>
  </main>
</body>
</html>
```